Packaging and labelling for Swiss made Organic CBD Oil

Visit our website www.velmarotiva.com
We have not put any product on yet as require packaging and label design .
Website will give you a great feel for the company and how we have used
the logo . The Drevask cbd product shown is a company similar to ourselves with similar core values , we liked the clean packaging design they have .

Im happy if you want use the mandala symbol in our logo separate from
VELMARO, to separate and use the mandala symbol as a larger icon than
it appears in our logo
Clean , Pure , organic feel. Like the product to look pharmaceutical and life changing not gimmicky.
Colours to go with or be the same as our logo colours
But not too cold and clinical
Bottle size 84mm x 25mm
Label size 75mm x 30mm
Box 30mm x 30mm x 100mm
6 products
Full Spectrum :
500mg CBD (5%)
1000mg CBD ( 10% )
1500mg CBD (15%)
2000mg CBD ( 20% )
Broad spectrum THC Free
500mg CBD (5%)
Pets
500mg Broad Spectrum THC Free
Updates

Would like the design to be more modern than traditional

LABEL Information Front of Bottle - Logo VELMARO & Mandala - Mandala can be used separately as design symbol Organic Cannabis Oil 1500mg CBD (15%) Ful Spectrum 10ml Back of bottle Ingredients: Organic Cannabis Oil Extract Organic Sunflower Seed Oil THC - 0.2% Certified Swiss Organic Cultivation Shake well before use. Store in a cool , dry place and out of the each of children BOX information Front and rear Logo - VELMARO & Mandala - Mandala can be used separately as a design symbol Organic Cannabis Oil 1500mg CBD (15%) Full Spectrum Sides x 2 This product is a food supplement and is not intended to diagnose, treat, cure or prevent any disease If you are pregnant, lactating or taking any medication consult your health care practitioner Suitable for vegetarians and vegans Ingredients Organic Cannabis Oil extract Organis Sunflower Oil Store in a cool ,dry place, out of the reach of children Recommended Use 1-5 drops ( 1 drop = 7.5mg CBD ) Subject to body weight and personal requirement - visit www.velmarotiva for more information 100% Natural 100% Organic GMO free 100% Vegan ( symbol with each ) Expiry date see bottle label Cultivated and manufactured in Switzerland

Target Market(s)

age 40 - 80

Font styles to use
Other font styles liked:
• In our website we have used Open Sans for the copy and Lato for headings .

Requirements
Must have
• look like an Industry leader
Velmaro will change the quality of peoples lives and in some cases may
even save lives so want look powerful and credible
Our Mission is - Through Delivering Pure , Premium , Organic products we will educate, inform and help people achieve healthier , happier lifestyles
Nice to have
• Colours to look good with our logo colours or be the same as our logo
colours
Logo Font - Avenir Black and Avenir Book

Font used in website - Content - Open Sans / Headings - Lato
If you have another font for the packaging information that will go well with
our logo, I'm happy for you to use your skills

```html
<!DOCTYPE html>
<html lang="en">
<head>
<meta charset="utf-8">
<title>VELMARO – Organic Cannabis Oil Bottle Label</title>
<link href="https://fonts.googleapis.com/css2?family=Lato:wght@300;400;700&display=swap" rel="stylesheet">
<style>
  :root {
    --page-bg: #ffffff;
    --label-bg: #ffffff;
    --label-edge: #d4d4d4;
    --teal-band: #9fdcdc;
    --teal-tint: #e2f4f4;
    --ink: #4f4f4f;
    --ink-soft: #5e5e5e;
    --heading: #6a6a6a;
    --badge-line: #2e2e2e;
  }
  * { margin: 0; padding: 0; box-sizing: border-box; }
  html, body {
    width: 1200px; height: 900px; overflow: hidden;
    background: var(--page-bg);
    font-family: "Lato", sans-serif;
    color: var(--ink);
  }
  .canvas {
    position: relative; width: 1200px; height: 900px;
    display: flex; align-items: center; justify-content: center;
  }
  .bottle-label {
    position: relative; width: 1000px; height: 400px;
    background: var(--label-bg);
    border: 1.5px solid var(--label-edge);
    border-radius: 18px; overflow: hidden;
    box-shadow: 0 2px 6px rgba(0,0,0,0.08);
  }
  .label-band {
    position: absolute; left: 0; right: 0; bottom: 0; height: 116px;
    background: var(--teal-band);
  }
  .info-column {
    position: absolute; top: 36px; width: 262px;
    font-weight: 300; font-size: 18.5px; line-height: 22.5px;
    text-align: justify; color: var(--ink);
  }
  .info-column p + p { margin-top: 6px; }
  .info-column--notice { left: 24px; }
  .info-column--ingredients { left: 717px; }
  .info-column em { font-style: italic; font-weight: 700; }
  .certification-note {
    position: absolute; left: 24px; top: 231px;
    background: var(--teal-tint);
    padding: 1px 10px 2px 5px;
    font-weight: 300; font-size: 16.5px; color: var(--ink);
  }
  .brand-block {
    position: absolute; left: 350px; width: 300px; top: 192px; text-align: center;
  }
  .brand-name {
    font-weight: 700; font-size: 48px; letter-spacing: 3px; line-height: 1;
    color: var(--heading);
  }
  .brand-descriptor {
    margin-top: 6px; font-weight: 400; font-size: 24px; color: var(--ink-soft);
  }
  .strength-block {
    position: absolute; left: 350px; width: 300px; bottom: 6px;
    text-align: center; color: var(--ink);
  }
  .strength-block .dose { font-weight: 400; font-size: 21px; line-height: 34px; }
  .strength-block .spectrum { font-weight: 400; font-size: 23px; letter-spacing: 1.5px; line-height: 36px; }
  .strength-block .volume { font-weight: 300; font-size: 22px; line-height: 32px; }
  .storage-note {
    position: absolute; left: 715px; bottom: 42px; width: 280px;
    font-weight: 300; font-size: 18px; line-height: 22.5px; color: var(--ink);
  }
  .product-badges {
    position: absolute; left: 34px; bottom: 32px; display: flex; gap: 10px;
  }
  .product-badges svg { width: 48px; height: 48px; }
</style>
</head>
<body>
<main class="canvas">
  <section class="bottle-label" aria-label="Bottle label, 75 × 30 mm">
    <div class="label-band"></div>

    <div class="info-column info-column--notice">
      <p>This product is a food supplement and is not intended to diagnose, treat, cure or prevent any disease If you are pregnant, lactating or taking any medication consult your health care practitioner Suitable for vegetarians and vegans</p>
    </div>
    <span class="certification-note">Certified Swiss Organic Cultivation</span>

    <div class="brand-block">
      <h1 class="brand-name">VELMARO</h1>
      <p class="brand-descriptor">Organic Cannabis Oil</p>
    </div>

    <div class="info-column info-column--ingredients">
      <p><em>Ingredients:</em> Organic Cannabis Oil Extract Organic Sunflower Seed Oil THC - 0.2%</p>
      <p>Organic Cannabis Oil extract Organis Sunflower Oil Store in a cool ,dry place, out of the reach of children Recommended Use 1-5 drops ( 1 drop = 7.5mg CBD ) Subject to body weight and personal requirement</p>
    </div>

    <div class="product-badges" aria-label="Product certification badges">
      <svg viewBox="0 0 48 48"><circle cx="24" cy="24" r="21" fill="none" stroke="var(--badge-line)" stroke-width="3"/></svg>
      <svg viewBox="0 0 48 48"><circle cx="24" cy="24" r="21" fill="none" stroke="var(--badge-line)" stroke-width="3"/></svg>
      <svg viewBox="0 0 48 48"><circle cx="24" cy="24" r="21" fill="none" stroke="var(--badge-line)" stroke-width="3"/></svg>
      <svg viewBox="0 0 48 48"><circle cx="24" cy="24" r="21" fill="none" stroke="var(--badge-line)" stroke-width="3"/></svg>
    </div>

    <div class="strength-block">
      <p class="dose">1500mg CBD (15%)</p>
      <p class="spectrum">FUL SPECTRUM</p>
      <p class="volume">10ml</p>
    </div>

    <p class="storage-note">Shake well before use.<br>Store in a cool , dry place and out of the each of children</p>
  </section>
</main>
</body>
</html>
```